Modern business card design for professional copywriter

I'd like a business card design that I can use to have my cards printed out by plink.com as a squared corners business card (see artwork and design guidelines here: https://help.plink.com/hc/en-gb/sections/300481726-PLINK-Product-Templates)

The design should be clean and modern and reflect the colours, tone and branding on my website: https://noravestrel.com.au

Target Market(s)

Professionals, B2B small business owners

Industry/Entity Type

Business

Contact Information for Business Card

Nora Vestrel
m: 0427 593 864
e: nora@noravestrel.com.au
w: noravestrel.com.au

Font styles to use
Sans Serif

Requirements
Must have
• Tagline: "Sharp, simple copy for busy business owners"
• Brand colours: fd8000, 009984, 666666 and black
Nice to have

```html
<!DOCTYPE html>
<html lang="en">
<head>
<meta charset="utf-8">
<title>Nora Vestrel – Copywriter Business Card</title>
<link rel="stylesheet" href="https://fonts.googleapis.com/css2?family=Quicksand:wght@500;700&family=Lato:wght@400;700&display=swap">
<style>
  :root {
    --brand-orange: #fd8000;
    --brand-teal: #009984;
    --brand-grey: #666666;
    --brand-black: #1f1f1f;
    --card-white: #ffffff;
    --backdrop: #e6e6e6;
  }
  * { box-sizing: border-box; margin: 0; padding: 0; }
  html, body { width: 1200px; height: 810px; overflow: hidden; }
  body {
    background: var(--backdrop);
    display: flex;
    align-items: center;
    justify-content: center;
    gap: 40px;
    font-family: "Lato", sans-serif;
  }
  .card {
    position: relative;
    width: 520px;
    height: 336px;
    overflow: hidden;
  }

  /* Front face */
  .card--front { background: var(--brand-black); }
  .brand {
    display: flex;
    align-items: center;
    gap: 10px;
    font-family: "Quicksand", sans-serif;
    font-weight: 700;
    color: var(--brand-teal);
    white-space: nowrap;
  }
  .brand__square {
    background: var(--brand-orange);
    flex: none;
  }
  .card--front .brand {
    position: absolute;
    left: 0; right: 0; top: 108px;
    justify-content: center;
    font-size: 46px;
  }
  .card--front .brand__square { width: 30px; height: 30px; }
  .tagline {
    position: absolute;
    left: 0; right: 0; bottom: 66px;
    text-align: center;
    font-family: "Quicksand", sans-serif;
    font-weight: 500;
    font-size: 15px;
    letter-spacing: 0.3px;
    color: var(--brand-teal);
  }

  /* Back face */
  .card--back { background: var(--card-white); }
  .card--back .brand {
    position: absolute;
    left: 34px; top: 64px;
    font-size: 25px;
    gap: 7px;
  }
  .card--back .brand__square { width: 16px; height: 16px; }
  .accent-circle {
    position: absolute;
    right: 40px; top: 64px;
    width: 150px; height: 150px;
    border-radius: 50%;
    background: var(--brand-orange);
    opacity: 0.9;
  }
  .contact {
    position: absolute;
    left: 34px; bottom: 34px;
  }
  .contact__name {
    font-family: "Quicksand", sans-serif;
    font-weight: 700;
    font-size: 22px;
    color: var(--brand-orange);
    margin-bottom: 12px;
  }
  .contact__list { list-style: none; }
  .contact__item {
    display: flex;
    align-items: center;
    gap: 7px;
    font-size: 14px;
    color: var(--brand-grey);
    line-height: 21px;
    white-space: nowrap;
  }
  .contact__icon { width: 12px; height: 12px; fill: var(--brand-orange); flex: none; }
</style>
</head>
<body>
  <section class="card card--front" aria-label="Business card front">
    <div class="brand"><span class="brand__square"></span>Nora Vestrel</div>
    <p class="tagline">Sharp, simple copy for busy business owners</p>
  </section>

  <section class="card card--back" aria-label="Business card back">
    <div class="brand"><span class="brand__square"></span>Nora Vestrel</div>
    <div class="accent-circle"></div>
    <div class="contact">
      <h1 class="contact__name">Nora Vestrel</h1>
      <ul class="contact__list">
        <li class="contact__item">
          <svg class="contact__icon" viewBox="0 0 24 24" aria-hidden="true"><path d="M6.6 10.8a15.1 15.1 0 0 0 6.6 6.6l2.2-2.2a1 1 0 0 1 1-.25 11.4 11.4 0 0 0 3.6.57 1 1 0 0 1 1 1V20a1 1 0 0 1-1 1A17 17 0 0 1 3 4a1 1 0 0 1 1-1h3.5a1 1 0 0 1 1 1 11.4 11.4 0 0 0 .57 3.6 1 1 0 0 1-.25 1z"/></svg>
          0427 593 864
        </li>
        <li class="contact__item">
          <svg class="contact__icon" viewBox="0 0 24 24" aria-hidden="true"><path d="M2 5h20l-10 7z"/><path d="M2 7l10 7 10-7v12H2z"/></svg>
          nora@noravestrel.com.au
        </li>
        <li class="contact__item">
          <svg class="contact__icon" viewBox="0 0 24 24" aria-hidden="true"><circle cx="12" cy="12" r="10"/><path d="M2 12h20M12 2c3 3 3 17 0 20M12 2c-3 3-3 17 0 20" stroke="#fff" stroke-width="1.6" fill="none"/></svg>
          noravestrel.com.au
        </li>
      </ul>
    </div>
  </section>
</body>
</html>
```